Awesome Redesign of Plumbing website

A great website designer to create this page for us in Wordpress with elementor.

- You are redesigning this site: http://fjellbekkror.no/

- Brand name is : Vannlinje Nord

- You can take pictures from the website or the one i attach, or stock images or AI generated images etc.

- The main call to action is to call the phone number (+47 23 86 51 94)
So please make that a priority.
- Mobile responsiveness is very important.
- The background should be white. You can use the color code red, white and black when you create the site.

I want you to build the website with a high speed score.

Target Market(s)

Residential market in oslo, Norway

Industry/Entity Type

Plumbing

Coding

Coded - Design and coding required

Requirements
Must have
• Build with elementor (wordpress), SEO friendly, A good CTA for phone, mobile responsive. Fast loading time. A Clean design.
Should not have
• Stock images that look "fake". All pictures have an authentic feel.

```html
<!DOCTYPE html>
<html lang="en">
<head>
<meta charset="utf-8">
<title>Vannlinje Nord – Plumber Oslo</title>
<link href="https://fonts.googleapis.com/css2?family=Roboto:wght@400;500;700;900&display=swap" rel="stylesheet">
<style>
:root{
  --red:#e3121b;
  --red-dark:#b80c13;
  --black:#111111;
  --charcoal:#2b2b2b;
  --grey:#6d6d6d;
  --line:#e2e2e2;
  --white:#ffffff;
  --amber:#f7a21b;
}
*{box-sizing:border-box;margin:0;padding:0}
html,body{width:1200px;height:4784px;overflow:hidden}
body{font-family:"Roboto",Arial,sans-serif;color:var(--black);background:var(--white);position:relative}
.btn{display:inline-block;background:var(--red);color:var(--white);font-weight:700;font-size:15px;letter-spacing:.5px;padding:14px 30px;border-radius:3px;text-transform:uppercase}
.photo{position:absolute}
h2.section-title{font-size:30px;font-weight:900;text-align:center;text-transform:uppercase;letter-spacing:.5px}

/* header + hero */
.hero{position:absolute;left:0;top:0;width:1200px;height:680px;background:linear-gradient(100deg,#15181c 0%,#2a2f35 45%,#4a4e53 70%,#2b2e33 100%)}
.nav{position:absolute;left:0;top:0;width:1200px;height:62px;display:flex;align-items:center;padding:0 120px;background:rgba(0,0,0,.35)}
.logo{color:var(--red);font-weight:900;font-size:24px;letter-spacing:1px;text-transform:uppercase}
.nav-links{display:flex;gap:34px;margin-left:auto;margin-right:30px;font-size:14px;color:var(--white)}
.nav-cta{background:var(--red);color:var(--white);font-size:13px;font-weight:700;padding:10px 18px;border-radius:3px;text-transform:uppercase}
.hero h1{position:absolute;left:120px;top:236px;font-size:58px;line-height:1.08;font-weight:900;color:var(--white);text-transform:uppercase}
.hero p{position:absolute;left:120px;top:378px;font-size:20px;color:var(--white)}
.hero .btn{position:absolute;left:120px;top:430px}

.callbar{position:absolute;left:0;top:680px;width:1200px;height:92px;background:var(--red);color:var(--white)}
.callbar .call{position:absolute;left:120px;top:20px}
.callbar .call small{display:block;font-size:14px;font-weight:700;letter-spacing:1px}
.callbar .call strong{font-size:30px;font-weight:900}
.area-form{position:absolute;left:350px;top:12px;width:520px}
.area-form label{display:block;font-size:14px;font-weight:700;text-align:center;margin-bottom:8px}
.area-form .row{display:flex;gap:10px}
.area-form .field{flex:1;height:38px;background:var(--white);border-radius:2px;color:var(--grey);font-size:13px;padding:11px 12px}
.area-form .go{width:110px;height:38px;background:var(--amber);color:var(--white);font-weight:700;font-size:13px;text-align:center;padding-top:11px;border-radius:2px}

/* services */
.services h2{position:absolute;left:0;top:826px;width:1200px}
.svc{position:absolute;width:232px;height:272px;border:1px solid var(--line);background:var(--white)}
.svc .pic{height:200px}
.svc .ico{position:absolute;left:92px;top:176px;width:48px;height:48px;border-radius:50%;background:var(--red);display:flex;align-items:center;justify-content:center;border:3px solid var(--white)}
.svc .label{position:absolute;left:0;bottom:0;width:100%;height:72px;display:flex;align-items:center;justify-content:center;text-align:center;font-weight:700;font-size:16px;text-transform:uppercase;padding:18px 10px 0}
.svc.active{background:var(--red);border-color:var(--red)}
.svc.active .label{color:var(--white)}
.svc.active .ico{background:var(--white);border-color:var(--red)}

/* testimonials */
.trust{position:absolute;left:0;top:1632px;width:1200px;height:448px;background:linear-gradient(180deg,#2a2a2a,#1c1c1c)}
.trust h2{position:absolute;left:0;top:56px;width:1200px;color:var(--white)}
.quote{position:absolute;top:124px;width:330px;height:212px;background:var(--white);border-radius:4px;padding:20px 24px;text-align:center}
.quote h3{font-size:20px;font-weight:700}
.quote .stars{color:var(--amber);font-size:22px;letter-spacing:2px;margin:6px 0 10px}
.quote p{font-size:14px;line-height:1.5;color:var(--charcoal)}
.quote cite{display:block;text-align:right;font-size:13px;font-style:normal;color:var(--grey);margin-top:8px}
.arrow{position:absolute;top:218px}

/* about */
.about-text{position:absolute;left:608px;top:2176px;width:472px}
.about-text h2{font-size:28px;line-height:1.25;font-weight:900;text-transform:uppercase;margin-bottom:18px}
.about-text p{font-size:14px;line-height:1.6;color:var(--charcoal);margin-bottom:12px}

/* why choose */
.why h2{position:absolute;left:0;top:2584px;width:1200px}
.feat{position:absolute;display:flex;align-items:center;gap:12px;font-size:15px;font-weight:500;width:220px}
.feat.left{flex-direction:row-reverse;text-align:right}
.feat .dot{flex:none;width:44px;height:44px;border-radius:50%;background:var(--red);display:flex;align-items:center;justify-content:center}

/* company band */
.company{position:absolute;left:0;top:2892px;width:1200px;height:428px;background:linear-gradient(180deg,#262626,#141414);color:var(--white);text-align:center}
.company h2{position:absolute;left:0;top:58px;width:1200px;font-size:30px;line-height:1.25;font-weight:900;text-transform:uppercase}
.company p{position:absolute;left:220px;top:156px;width:760px;font-size:14px;line-height:1.65;color:#e6e6e6}
.company .btn{position:absolute;left:528px;top:320px}

/* certificates */
.certs h2{position:absolute;left:0;top:3380px;width:1200px}
.badge{position:absolute;top:3438px;width:128px;height:100px;border:2px solid var(--red);border-radius:6px;display:flex;align-items:center;justify-content:center}
.badge span{display:block;width:70px;height:46px;background:#d6d6d6;border-radius:4px}

/* contact */
.contact-card{position:absolute;left:120px;top:3656px;width:340px;height:440px;background:var(--white);box-shadow:0 6px 24px rgba(0,0,0,.18);padding:28px 26px}
.contact-card h2{font-size:28px;font-weight:900;text-align:center;margin-bottom:20px}
.input{height:38px;border:1px solid #cfcfcf;border-radius:2px;font-size:13px;color:var(--grey);padding:11px 12px;margin-bottom:10px}
.input.area{height:78px}
.contact-card .btn{padding:11px 26px;font-size:14px}

/* appointment */
.appoint{position:absolute;left:0;top:4140px;width:1200px;height:288px;overflow:hidden;background:linear-gradient(120deg,#c40f17,#e3121b 55%,#9e0a10)}
.appoint h2{position:absolute;left:0;top:40px;width:1200px;text-align:center;color:var(--white);font-size:40px;line-height:1.15;font-weight:900;text-transform:uppercase}
.appoint .sub{position:absolute;left:0;top:142px;width:1200px;text-align:center;color:var(--white);font-size:16px}
.appoint .callnow{position:absolute;left:330px;top:184px;display:flex;align-items:center;gap:16px;color:var(--white)}
.appoint .callnow .circle{width:64px;height:64px;border-radius:50%;background:var(--white);display:flex;align-items:center;justify-content:center}
.appoint .callnow small{display:block;font-size:15px;font-weight:700}
.appoint .callnow strong{font-size:34px;font-weight:900}

/* footer */
.footer{position:absolute;left:0;top:4428px;width:1200px;height:356px;background:var(--black);color:#cfcfcf}
.fcol{position:absolute;top:52px}
.fcol h4{color:var(--red);font-size:16px;font-weight:700;text-transform:uppercase;margin-bottom:16px}
.fcol p,.fcol li{font-size:13px;line-height:1.7}
.fcol ul{list-style:none}
.fcol li{display:flex;align-items:center;gap:8px}
.fcol li i{display:inline-block;width:12px;height:12px;border-radius:50%;background:var(--red)}
.news{height:34px;background:var(--white);color:var(--grey);font-size:12px;padding:10px;width:220px;margin-bottom:10px}
.sub-btn{display:inline-block;background:var(--red);color:var(--white);font-size:13px;font-weight:700;padding:9px 20px}
.copy{position:absolute;left:0;bottom:0;width:1200px;height:46px;border-top:1px solid #2e2e2e;text-align:center;font-size:12px;padding-top:16px;color:#9a9a9a}
</style>
</head>
<body>

<section class="hero">
  <div class="photo" role="img" aria-label="Two smiling plumbers in black work sweaters standing beside a company van" style="left:600px;top:62px;width:600px;height:618px;background:radial-gradient(ellipse at 55% 55%,#5a5e63 0%,#36393d 55%,rgba(30,32,36,0) 80%)"></div>
  <nav class="nav">
    <div class="logo">Vannlinje Nord</div>
    <div class="nav-links"><span>Home</span><span>Services</span><span>About us</span><span>Environment and quality</span></div>
    <div class="nav-cta">Contact us</div>
  </nav>
  <h1>Vannlinje Nord AS<br>Plumber Oslo</h1>
  <p>We help you with all work related to plumbing.</p>
  <span class="btn">Get started</span>
</section>

<div class="callbar">
  <div class="call"><small>CALL NOW</small><strong>+47 23 86 51 94</strong></div>
  <div class="area-form">
    <label>IN WHICH AREA DO YOU WANT HELP?</label>
    <div class="row"><div class="field">In Oslo</div><div class="field">Outside of Oslo</div><div class="go">SUBMIT</div></div>
  </div>
</div>
<div class="photo" role="img" aria-label="Black company service van with red graphics" style="left:910px;top:636px;width:270px;height:170px;border-radius:26px 40px 14px 14px;background:linear-gradient(180deg,#2c2c2c,#0e0e0e)"></div>

<section class="services">
  <h2 class="section-title">A few selected services:</h2>

  <div class="svc" style="left:120px;top:888px">
    <div class="pic" role="img" aria-label="Modern tiled wet room with shower" style="background:linear-gradient(160deg,#d9d9d9,#9c9c9c)"></div>
    <div class="ico"><svg width="24" height="24" viewBox="0 0 24 24"><path d="M4 11h16v3a6 6 0 0 1-6 6h-4a6 6 0 0 1-6-6z" fill="#fff"/><rect x="6" y="4" width="3" height="7" fill="#fff"/></svg></div>
    <div class="label">Wet room</div>
  </div>
  <div class="svc active" style="left:368px;top:888px">
    <div class="pic" role="img" aria-label="Red pipes and valves in a utility room" style="background:linear-gradient(160deg,#f0a0a3,#b01a20)"></div>
    <div class="ico"><svg width="24" height="24" viewBox="0 0 24 24"><path d="M3 9h10v-4h4v14h-4v-6H3z" fill="#e3121b"/></svg></div>
    <div class="label">Clogged drain pipes</div>
  </div>
  <div class="svc" style="left:616px;top:888px">
    <div class="pic" role="img" aria-label="Outdoor heat pump units" style="background:linear-gradient(160deg,#cfcfcf,#858585)"></div>
    <div class="ico"><svg width="24" height="24" viewBox="0 0 24 24"><rect x="3" y="5" width="18" height="14" rx="2" fill="none" stroke="#fff" stroke-width="2"/><circle cx="12" cy="12" r="4" fill="none" stroke="#fff" stroke-width="2"/></svg></div>
    <div class="label">Heat pumps</div>
  </div>
  <div class="svc" style="left:864px;top:888px">
    <div class="pic" role="img" aria-label="Water leaking from a pipe joint" style="background:linear-gradient(160deg,#d4d4d4,#7a7a7a)"></div>
    <div class="ico"><svg width="24" height="24" viewBox="0 0 24 24"><path d="M12 3C9 8 6 11 6 14.5a6 6 0 0 0 12 0C18 11 15 8 12 3z" fill="#fff"/></svg></div>
    <div class="label">Water leakage</div>
  </div>

  <div class="svc" style="left:244px;top:1240px">
    <div class="pic" role="img" aria-label="Plumber working on pipes under a sink" style="background:linear-gradient(160deg,#d2d2d2,#8a8a8a)"></div>
    <div class="ico"><svg width="24" height="24" viewBox="0 0 24 24"><path d="M14 3a5 5 0 0 0-4.6 6.9L3 16.3 5.7 19l6.4-6.4A5 5 0 0 0 19 8l-3 1-2-2 1-3z" fill="#fff"/></svg></div>
    <div class="label">Plumber on duty</div>
  </div>
  <div class="svc" style="left:492px;top:1240px">
    <div class="pic" role="img" aria-label="Brass pressure reducing valve with gauge" style="background:linear-gradient(160deg,#cacaca,#7e7e7e)"></div>
    <div class="ico"><svg width="24" height="24" viewBox="0 0 24 24"><circle cx="12" cy="12" r="8" fill="none" stroke="#fff" stroke-width="2"/><path d="M12 12l4-4" stroke="#fff" stroke-width="2"/></svg></div>
    <div class="label">Pressure reducing valve</div>
  </div>
  <div class="svc" style="left:740px;top:1240px">
    <div class="pic" role="img" aria-label="Plumber tightening a pipe with a wrench" style="background:linear-gradient(160deg,#d0d0d0,#777)"></div>
    <div class="ico"><svg width="24" height="24" viewBox="0 0 24 24"><path d="M12 3l9 17H3z" fill="#fff"/><rect x="11" y="9" width="2" height="6" fill="#e3121b"/><rect x="11" y="16" width="2" height="2" fill="#e3121b"/></svg></div>
    <div class="label">Emergency help</div>
  </div>
</section>

<section class="trust">
  <h2 class="section-title">Long experience you can trust</h2>
  <svg class="arrow" style="left:108px" width="24" height="24" viewBox="0 0 24 24"><path d="M15 4l-8 8 8 8" stroke="#fff" stroke-width="3" fill="none"/></svg>
  <div class="quote" style="left:256px">
    <h3>Changing the toilet.</h3>
    <div class="stars">★★★★★</div>
    <p>Vannlinje Nord did the job in an excellent way. They sent a nice and good plumber who was there within 20 minutes. Recommended</p>
    <cite>-Ingrid Solberg Haug</cite>
  </div>
  <div class="quote" style="left:614px">
    <h3>Faucet leaking</h3>
    <div class="stars">★★★★★</div>
    <p>Vannlinje Nord was very quick to respond to the job assignment. Satisfied with the job performance. Nice people.</p>
    <cite>-Arne Toresen Lie</cite>
  </div>
  <svg class="arrow" style="left:1068px" width="24" height="24" viewBox="0 0 24 24"><path d="M9 4l8 8-8 8" stroke="#fff" stroke-width="3" fill="none"/></svg>
</section>

<section class="about">
  <div class="photo" role="img" aria-label="Two plumbers in black sweaters standing side by side indoors" style="left:120px;top:2128px;width:448px;height:400px;background:linear-gradient(150deg,#cfcfcf,#6f6f6f 60%,#2e2e2e)"></div>
  <div class="about-text">
    <h2>We are a good alternative<br>when you want help with plumbing</h2>
    <p>For several years, homeowners and housing associations throughout Oslo have trusted us with their plumbing. We are valued for honest advice, tidy work, good availability and prices that are easy to understand.</p>
    <p>Many years in the trade have given us the experience needed to plan every job properly. We are happy to come out for an inspection, give a clear written offer and explain exactly what will be done. Our skilled plumbers make sure every detail is solved the right way, so the result lasts for many years.</p>
    <span class="btn">Learn more</span>
  </div>
</section>

<section class="why">
  <h2 class="section-title">Why choose Vannlinje Nord?</h2>
  <div class="feat left" style="left:150px;top:2650px"><span class="dot"><svg width="20" height="20" viewBox="0 0 24 24"><path d="M4 12l5 5 11-11" stroke="#fff" stroke-width="3" fill="none"/></svg></span><span>Non-binding and reasonable prices</span></div>
  <div class="feat left" style="left:150px;top:2718px"><span class="dot"><svg width="20" height="20" viewBox="0 0 24 24"><circle cx="12" cy="12" r="8" fill="none" stroke="#fff" stroke-width="2.5"/><path d="M12 7v5h4" stroke="#fff" stroke-width="2.5" fill="none"/></svg></span><span>Always fixed price</span></div>
  <div class="feat left" style="left:150px;top:2786px"><span class="dot"><svg width="20" height="20" viewBox="0 0 24 24"><path d="M12 2a7 7 0 0 0-7 7c0 5 7 13 7 13s7-8 7-13a7 7 0 0 0-7-7z" fill="#fff"/></svg></span><span>Punctual arrival</span></div>
  <div class="photo" role="img" aria-label="Black company van with red side graphics" style="left:410px;top:2650px;width:380px;height:190px;border-radius:30px 60px 16px 16px;background:linear-gradient(180deg,#2a2a2a,#0c0c0c)"></div>
  <div class="feat" style="left:830px;top:2650px"><span class="dot"><svg width="20" height="20" viewBox="0 0 24 24"><circle cx="12" cy="9" r="5" fill="#fff"/><path d="M8 13l-2 8 6-3 6 3-2-8" fill="#fff"/></svg></span><span>Only certified and trained plumbers</span></div>
  <div class="feat" style="left:830px;top:2718px"><span class="dot"><svg width="20" height="20" viewBox="0 0 24 24"><path d="M4 12l5 5 11-11" stroke="#fff" stroke-width="3" fill="none"/></svg></span><span>Competitive prices</span></div>
  <div class="feat" style="left:830px;top:2786px"><span class="dot"><svg width="20" height="20" viewBox="0 0 24 24"><path d="M12 3l2.6 5.6 6 .7-4.5 4.1 1.2 6L12 16.5 6.7 19.4l1.2-6L3.4 9.3l6-.7z" fill="#fff"/></svg></span><span>Job done right the first time</span></div>
</section>

<section class="company">
  <h2>Our plumbing company in Oslo offers good and<br>affordable plumbing help</h2>
  <p>When renovating a bathroom or wet room, the plumbing company can take responsibility for the entire project and coordinate work that must be carried out by other types of craftsmen. Plumbers saw and finish surfaces, so that you do not risk leaks and can use the bathroom as you wish. There are strict requirements for the treatment of floors and walls in wet rooms. Many people want to use the space in bathrooms, especially in small apartments, and then you often want to choose where the floor drain should be placed. Whether you choose to deal with a bathroom or simply a repair, the plumbing company will ensure that the floor, drains and walls meet all regulations and rules.</p>
  <span class="btn">Learn more</span>
</section>

<section class="certs">
  <h2 class="section-title">Certificate</h2>
  <div class="badge" style="left:142px"><span></span></div>
  <div class="badge" style="left:298px"><span></span></div>
  <div class="badge" style="left:454px"><span></span></div>
  <div class="badge" style="left:610px"><span></span></div>
  <div class="badge" style="left:766px"><span></span></div>
  <div class="badge" style="left:922px"><span></span></div>
</section>

<section class="contact">
  <div class="photo" role="img" aria-label="Street map of central Oslo" style="left:0;top:3592px;width:1200px;height:548px;background:linear-gradient(135deg,#e7ece2,#dfe6e9 50%,#e9e7df)"></div>
  <div class="contact-card">
    <h2>GET IN TOUCH</h2>
    <div class="input">Name</div>
    <div class="input">Address</div>
    <div class="input">Email</div>
    <div class="input">Phone</div>
    <div class="input area">Message</div>
    <span class="btn">Submit</span>
  </div>
</section>

<section class="appoint">
  <h2>Would you like to set up<br>an appointment with Vannlinje Nord?</h2>
  <div class="sub">We will be in touch with you to verify your appointment.</div>
  <div class="callnow">
    <span class="circle"><svg width="30" height="30" viewBox="0 0 24 24"><path d="M6.6 10.8a15 15 0 0 0 6.6 6.6l2.2-2.2a1 1 0 0 1 1-.25 11.4 11.4 0 0 0 3.6.6 1 1 0 0 1 1 1V20a1 1 0 0 1-1 1A17 17 0 0 1 3 4a1 1 0 0 1 1-1h3.5a1 1 0 0 1 1 1c0 1.25.2 2.45.6 3.6a1 1 0 0 1-.25 1z" fill="#e3121b"/></svg></span>
    <div><small>NEED HELP NOW ?</small><strong>CALL:+47 23 86 51 94</strong></div>
  </div>
  <div class="photo" role="img" aria-label="Black company van parked" style="left:900px;top:158px;width:280px;height:130px;border-radius:26px 46px 0 0;background:linear-gradient(180deg,#2a2a2a,#0c0c0c)"></div>
</section>

<footer class="footer">
  <div class="fcol" style="left:120px;width:230px">
    <h4>Vannlinje Nord</h4>
    <p>Whether you are renovating, converting or just need a quick repair, we are ready to help. Contact us today and get a fixed price offer without obligation.</p>
  </div>
  <div class="fcol" style="left:420px">
    <h4>About</h4>
    <ul><li>Home</li><li>Services</li><li>About us</li><li>Environment and quality</li></ul>
  </div>
  <div class="fcol" style="left:640px">
    <h4>Follow us</h4>
    <ul><li><i></i>Nabolag</li><li><i></i>Kvitter</li><li><i></i>Bildeflyt</li><li><i></i>Filmkanal</li></ul>
  </div>
  <div class="fcol" style="left:860px">
    <h4>Newsletter</h4>
    <div class="news">Email address</div>
    <span class="sub-btn">SUBSCRIBE</span>
  </div>
  <div class="copy">© 2022 Vannlinje Nord. All rights reserved</div>
</footer>

</body>
</html>
```